Doctors clinic requires stationary designed

We require various types of stationary to be design based on the logo (attached). We require the following:
- Letterhead (A4 Portrait)
- Business Card (must include UV spot on rear)
- With compliments slip (DL Landscape)
- Appointments card (Folded A6)

We are a young clinical practice which boasts a modern and sophisticated approach to medicine so we require something which feels fresh and modern. Please include colours represented in the logo (contrasting teal and grey). We are calling for creative minds to put forth their ideas and we will be actively providing feedback on all designs.

thank you

Clinic

```html
<!DOCTYPE html>
<html lang="en">
<head>
<meta charset="utf-8">
<title>Dr Clara Whitfield – With Compliments Slip</title>
<link rel="stylesheet" href="https://fonts.googleapis.com/css2?family=Open+Sans:wght@600&family=Pinyon+Script&family=Questrial&display=swap">
<style>
  :root {
    --teal: #2a8c84;
    --teal-soft: #d3e8e5;
    --grey: #9a9a9a;
    --grey-dark: #6f6f6f;
    --paper: #ffffff;
    --backdrop: #ececec;
  }
  * { margin: 0; padding: 0; box-sizing: border-box; }
  html, body {
    width: 1200px;
    height: 888px;
    overflow: hidden;
    background: var(--backdrop);
  }
  .canvas {
    position: relative;
    width: 1200px;
    height: 888px;
  }
  .slip {
    position: absolute;
    left: 100px;
    top: 208px;
    width: 1000px;
    height: 472px;
    background: var(--paper);
    overflow: hidden;
    box-shadow: 0 2px 10px rgba(0,0,0,0.08);
  }
  .brand {
    position: absolute;
    left: 44px;
    top: 44px;
    display: flex;
    align-items: center;
    gap: 14px;
  }
  .brand-dot {
    width: 58px;
    height: 58px;
    border: 3px solid var(--teal);
    border-radius: 50%;
  }
  .brand-name {
    font-family: "Open Sans", sans-serif;
    font-weight: 600;
    color: var(--teal);
    font-size: 25px;
    line-height: 1.1;
    letter-spacing: -0.3px;
  }
  .brand-role {
    font-family: "Open Sans", sans-serif;
    font-weight: 600;
    color: var(--teal);
    font-size: 14.5px;
    line-height: 1.3;
  }
  .greeting {
    position: absolute;
    right: 70px;
    top: 112px;
    font-family: "Pinyon Script", cursive;
    font-size: 58px;
    line-height: 1;
  }
  .greeting .with { color: var(--grey); margin-right: 18px; }
  .greeting .compliments { color: var(--teal); }
  .contact {
    position: absolute;
    left: 44px;
    top: 336px;
    display: flex;
    font-family: "Questrial", sans-serif;
    color: var(--grey-dark);
    font-size: 12.5px;
    line-height: 1.45;
  }
  .address {
    text-transform: uppercase;
    padding-right: 20px;
  }
  .address .city { text-transform: none; }
  .divider {
    width: 1px;
    height: 50px;
    background: #c9c9c9;
    margin-top: 6px;
  }
  .channels {
    list-style: none;
    padding-left: 20px;
    padding-top: 26px;
  }
  .channels li {
    display: flex;
    align-items: center;
    gap: 8px;
    font-size: 13px;
  }
  .channels svg { width: 12px; height: 12px; }
  .mark-decoration {
    position: absolute;
    left: 590px;
    top: 270px;
    width: 360px;
    height: 260px;
    border-radius: 50% 50% 0 0;
    background: radial-gradient(circle at 50% 60%, var(--teal-soft), rgba(211,232,229,0) 72%);
  }
</style>
</head>
<body>
<div class="canvas">
  <section class="slip">
    <header class="brand">
      <span class="brand-dot" aria-hidden="true"></span>
      <div>
        <p class="brand-name">Dr Clara Whitfield</p>
        <p class="brand-role">Obstetrician and Gynaecologist</p>
      </div>
    </header>

    <h1 class="greeting"><span class="with">With</span><span class="compliments">Compliments</span></h1>

    <footer class="contact">
      <address class="address">
        42 Linden Row<br>
        <span class="city">Maplewood, PA 17900</span>
      </address>
      <span class="divider" aria-hidden="true"></span>
      <ul class="channels">
        <li>
          <svg viewBox="0 0 12 12" aria-hidden="true">
            <circle cx="6" cy="6" r="6" fill="var(--teal)"/>
            <path d="M4 3.2c.4-.3.8-.2 1 .2l.4.8c.1.3 0 .5-.2.7l-.3.2c.3.7.8 1.2 1.5 1.5l.2-.3c.2-.2.4-.3.7-.2l.8.4c.4.2.5.6.2 1l-.4.4c-.4.4-1 .4-1.6.1-1.2-.6-2.1-1.5-2.7-2.7-.3-.6-.3-1.2.1-1.6z" fill="#fff"/>
          </svg>
          (555) 014-2288
        </li>
        <li>
          <svg viewBox="0 0 12 12" aria-hidden="true">
            <circle cx="6" cy="6" r="6" fill="var(--teal)"/>
            <rect x="3" y="4" width="6" height="4.2" rx="0.5" fill="#fff"/>
            <path d="M3.2 4.3 6 6.4l2.8-2.1" fill="none" stroke="var(--teal)" stroke-width="0.7"/>
          </svg>
          clara@whitfieldcare.com
        </li>
      </ul>
    </footer>

    <div class="mark-decoration" role="img" aria-label="Large teal brand mark decoration"></div>
  </section>
</div>
</body>
</html>
```